Tidewell Private Yacht Charter "Rack Flyer"

This will be a 4" x 9" Rack flyer that is 4 colors and two sided. This is a Private Yacht charter company that is based in St Thomas, U.S. Virgin Islands. Our main product that I would like to promote on one entire side of the flyer is our Private Luxury Full Day "Glimmer Feast". our charter company is unique in the fact we offer customizable itineraries and we offer unique activities that keep the family and groups engaged in fun for the entire day. We would like something with our colors.

Target Market(s)

We are trying to reach an upscale clients that are looking for a Luxury Day Charter experience. these people will be most likely staying in Private Villas or staying at the Halvern Crest or QP Delacourt.

Requirements
Must have
• Contact Information:
Ph: (340) 555-0187
email: Info@tidewellvi.example
www.tidewellvi.example
One side should Promote our Glimmer Feast (Glimmer Feast is a trademarked name).
All Guests will receive "Welcome Mimosas"
> Up to 12 guests
> Full Brunch Spread to include, Assorted fruit tower, Artesian Waffle Board, Frittata's, Loaded Avocado Toast or an All American Breakfast.
> Specialty Cocktails with Bottle Service options available
List all of our Unique activities to include:
Snorkeling
Underwater WaveGlider
Cliff Diving
Paddleboarding
Towable Activities
TEXT TO BE WRITTEN:
Experience yacht charter service at its Finest!
Sail away with us on a Luxury Charter experience complete with a full brunch spread. During our sail we will take you to the hottest destination spots in the Caribbean surrounding St Thomas and St John. Warm, fresh baked afternoon cookies will be served on the way back from our days journeys. Unlimited water, sodas, beer and rum punch will be provided for the entire group to enjoy throughout the day.
_________________

On side two of the brochure you can refer to the downloaded text. We do not want pricing listed on the flyer

```html
<!DOCTYPE html>
<html lang="en">
<head>
<meta charset="utf-8">
<title>Tidewell Private Yacht Charter – Rack Flyer</title>
<link href="https://fonts.googleapis.com/css2?family=Oswald:wght@300;400;500;600&family=Pathway+Gothic+One&family=Cinzel:wght@500&family=Playfair+Display:ital,wght@0,700;1,700&display=swap" rel="stylesheet">
<style>
:root{
  --red:#e5232b;
  --blue:#1b4ea3;
  --navy:#163f8c;
  --ink:#2b2b2b;
  --paper:#ffffff;
  --bg:#ececec;
  --sea:#2fb4cf;
  --sand:#e9c58f;
}
*{box-sizing:border-box;margin:0;padding:0}
html,body{width:1200px;height:993px;overflow:hidden;background:var(--bg)}
.stage{position:relative;width:1200px;height:993px}
.flyer{position:absolute;top:54px;width:393px;height:884px;background:var(--paper);overflow:hidden;box-shadow:0 4px 14px rgba(0,0,0,.12)}
.front{left:180px}
.back{left:628px}
.abs{position:absolute}

/* front */
.front .water{left:0;top:560px;width:393px;height:324px;background:linear-gradient(180deg,#dbe9f2 0%,#eef4f8 40%,#f6f8fa 100%)}
.brand{left:0;top:40px;width:393px;text-align:center;font-family:'Oswald',sans-serif;font-weight:500;font-size:40px;letter-spacing:3px;color:var(--red)}
.brand .dot{display:inline-block;width:14px;height:14px;border-radius:50%;background:var(--navy);margin-left:8px;vertical-align:middle}
.experience{left:0;top:118px;width:393px;text-align:center;font-family:'Cinzel',serif;font-weight:500;font-size:32px;letter-spacing:3px;color:var(--navy)}
.title-bar{left:38px;top:158px;width:318px;height:39px;background:var(--red);border-radius:6px 0 6px 0;color:#fff;font-family:'Oswald',sans-serif;font-size:26px;line-height:39px;text-align:center;letter-spacing:.3px}
.feature-name{left:0;top:196px;width:393px;text-align:center;font-family:'Playfair Display',serif;font-style:italic;font-weight:700;font-size:37px;color:var(--red)}
.photo{border-radius:50%}
.photo-boat{left:156px;top:250px;width:296px;height:296px;background:radial-gradient(circle at 55% 40%,#f4f4f2 0%,#d9ecef 35%,var(--sea) 70%,#1f8fb3 100%)}
.photo-snorkel{left:19px;top:242px;width:170px;height:170px;background:radial-gradient(circle at 40% 45%,#4a86a6,#1c4d78 80%);border:2px solid #fff}
.photo-brunch{left:18px;top:385px;width:200px;height:200px;background:radial-gradient(circle at 50% 60%,#e9b98f 0%,#c98c62 45%,#6ea5c4 100%);border:2px solid #fff}
.bullets{left:32px;top:646px;width:340px;font-family:'Oswald',sans-serif;font-weight:400;font-size:12.2px;color:var(--ink);line-height:17.5px;list-style:none}
.bullets li{position:relative;padding-left:20px;margin-bottom:2px}
.bullets li::before{content:"";position:absolute;left:2px;top:5px;width:8px;height:8px;border-radius:50%;background:var(--red)}
.guests-tag{left:269px;top:634px;width:98px;height:21px;background:var(--red);border-radius:4px 0 4px 0;color:#fff;font-family:'Oswald',sans-serif;font-weight:500;font-size:12px;line-height:21px;text-align:center}
.info-box{left:22px;top:744px;width:350px;height:84px;border:1px solid var(--navy);border-radius:3px}
.info-head{left:47px;top:732px;width:300px;height:21px;background:var(--red);border-radius:4px 0 4px 0;color:#fff;font-family:'Oswald',sans-serif;font-weight:500;font-size:12px;line-height:21px;text-align:center}
.info-text{left:32px;top:757px;width:330px;font-family:'Pathway Gothic One',sans-serif;font-size:9.8px;line-height:13.2px;color:var(--ink);text-align:center}
.phone{left:88px;top:816px;width:218px;height:28px;background:var(--red);border-radius:14px;color:#fff;font-family:'Oswald',sans-serif;font-weight:600;font-size:21px;line-height:28px;padding-left:40px}
.phone-icon{left:90px;top:816px;width:28px;height:28px}
.contacts{left:0;top:851px;width:393px;display:flex;justify-content:center;align-items:center;gap:8px;font-family:'Oswald',sans-serif;font-weight:400;font-size:12.5px;color:var(--ink)}
.contacts .sep{width:1px;height:14px;background:var(--ink)}
.contacts svg{vertical-align:-2px;margin-right:5px}

/* back */
.back .haze{left:0;top:250px;width:393px;height:634px;background:linear-gradient(180deg,#f1f5f8 0%,#eef2f0 50%,#f4f6f8 100%)}
.act-head{left:35px;top:29px;width:323px;height:32px;border:1.5px solid #fff;border-radius:3px;color:#fff;font-family:'Oswald',sans-serif;font-weight:500;font-size:18px;line-height:29px;text-align:center;letter-spacing:.2px}
.act-grid{left:35px;top:72px;width:340px;display:grid;grid-template-columns:95px 104px 1fr;row-gap:4px;font-family:'Oswald',sans-serif;font-weight:400;font-size:12.5px;color:#fff;list-style:none}
.tick{position:relative;padding-left:13px}
.tick::before{content:"";position:absolute;left:0;top:5px;width:9px;height:9px;border:1px solid currentColor;border-radius:50%}
.tick::after{content:"";position:absolute;left:3px;top:7px;width:3px;height:2px;border-left:1px solid currentColor;border-bottom:1px solid currentColor;transform:rotate(-45deg)}
.act-note{left:35px;top:142px;width:170px;font-family:'Pathway Gothic One',sans-serif;font-size:12.5px;line-height:15.5px;color:#fff}
.photo-family{left:204px;top:127px;width:166px;height:166px;background:radial-gradient(circle at 50% 45%,#f3e4d6,#bcd5e4 70%);border:3px solid var(--red)}
.photo-ray{left:119px;top:189px;width:110px;height:110px;background:radial-gradient(circle at 50% 55%,#a9d9d6,#3c9aa8 90%);border:3px solid var(--red)}
.types-bar{left:29px;top:307px;width:334px;height:39px;background:var(--red);border-radius:6px 0 0 0;color:#fff;font-family:'Playfair Display',serif;font-weight:700;font-size:24px;line-height:39px;text-align:center;letter-spacing:.5px}
.timeline{left:36px;top:372px;width:1px;height:478px;background:var(--red)}
.charter{left:20px;width:354px;padding-left:32px}
.charter .mark{position:absolute;left:9px;top:4px;width:14px;height:14px;border-radius:50%;border:1.2px solid var(--red);background:#fff;color:var(--red)}
.charter .mark::after{content:"";position:absolute;left:3px;top:3px;width:5px;height:3px;border-left:1.2px solid var(--red);border-bottom:1.2px solid var(--red);transform:rotate(-45deg)}
.charter h3{font-family:'Oswald',sans-serif;font-weight:500;font-size:16.5px;line-height:21px;color:var(--navy);letter-spacing:-.1px}
.charter h3 span{color:var(--red);font-weight:400}
.charter p{margin-top:3px;font-family:'Pathway Gothic One',sans-serif;font-size:7.9px;line-height:11.4px;color:var(--ink);text-align:justify}
</style>
</head>
<body>
<div class="stage">

  <!-- Side one: feature -->
  <section class="flyer front">
    <div class="abs water" role="img" aria-label="Faint turquoise sea water behind the details"></div>

    <div class="abs brand">TIDEWELL<span class="dot"></span></div>
    <div class="abs experience">EXPERIENCE</div>
    <div class="abs title-bar">PRIVATE LUXURY FULL DAY</div>
    <div class="abs feature-name">Glimmer Feast</div>

    <svg class="abs" style="left:0;top:300px" width="393" height="340" viewBox="0 0 393 340">
      <path d="M393 0 L393 45 L358 45 Z" fill="var(--red)"/>
      <path d="M0 70 L30 110 L0 135 Z" fill="var(--red)"/>
      <path d="M0 200 C60 290 190 300 393 250 L393 265 C200 330 70 320 0 260 Z" fill="var(--red)"/>
      <circle cx="322" cy="255" r="50" fill="#ef7466" opacity=".85"/>
      <circle cx="250" cy="290" r="36" fill="#ffffff" opacity=".55"/>
    </svg>

    <div class="abs photo photo-boat" role="img" aria-label="White luxury catamaran anchored in turquoise water beside a sandy beach"></div>
    <div class="abs photo photo-snorkel" role="img" aria-label="Couple snorkeling underwater with masks"></div>
    <div class="abs photo photo-brunch" role="img" aria-label="Guests toasting cocktails over a brunch table on deck"></div>

    <div class="abs guests-tag">UP TO 12 GUESTS</div>
    <ul class="abs bullets">
      <li>All Guests will receive "Welcome Mimosas"</li>
      <li>Full Brunch Spread to include, Assorted fruit tower, Artesian Waffle Board, Frittata's, Loaded Avocado Toast or an All American Breakfast.</li>
      <li>Specialty Cocktails with Bottle Service options available</li>
    </ul>

    <div class="abs info-box"></div>
    <div class="abs info-head">EXPERIENCE YACHT CHARTER SERVICE AT ITS FINEST!</div>
    <p class="abs info-text">Sail away with us on a Luxury Charter experience complete with a full brunch spread. During our sail we will take you to the hottest destination spots in the Caribbean surrounding St Thomas and St John. Warm, fresh baked afternoon cookies will be served on the way back from our days journeys. Unlimited water, sodas, beer and rum punch will be provided for the entire group to enjoy throughout the day.</p>

    <div class="abs phone">(340) 555-0187</div>
    <svg class="abs phone-icon" viewBox="0 0 28 28">
      <circle cx="14" cy="14" r="13" fill="var(--blue)" stroke="#fff" stroke-width="1.5"/>
      <path d="M10 8 L12.5 8 L13.5 11 L12 12.3 C12.8 14 14 15.2 15.7 16 L17 14.5 L20 15.5 L20 18 C20 19 19 19.8 18 19.6 C13 18.8 9.2 15 8.4 10 C8.2 9 9 8 10 8 Z" fill="none" stroke="#fff" stroke-width="1.2" stroke-linejoin="round"/>
    </svg>

    <div class="abs contacts">
      <span><svg width="13" height="10" viewBox="0 0 13 10"><rect x=".5" y=".5" width="12" height="9" fill="none" stroke="var(--red)"/><path d="M.5 .5 L6.5 5.5 L12.5 .5" fill="none" stroke="var(--red)"/></svg>Info@tidewellvi.example</span>
      <span class="sep"></span>
      <span><svg width="12" height="12" viewBox="0 0 12 12"><circle cx="6" cy="6" r="5.3" fill="none" stroke="var(--red)"/><path d="M.7 6 H11.3 M6 .7 C3 4 3 8 6 11.3 M6 .7 C9 4 9 8 6 11.3" fill="none" stroke="var(--red)" stroke-width=".8"/></svg>www.tidewellvi.example</span>
    </div>
  </section>

  <!-- Side two: activities and charters -->
  <section class="flyer back">
    <div class="abs haze" role="img" aria-label="Faded photo of a family celebrating with raised arms over a bay"></div>

    <svg class="abs" style="left:0;top:0" width="393" height="300" viewBox="0 0 393 300">
      <path d="M0 172 C60 215 120 240 190 236 L120 255 C70 258 30 250 0 232 Z" fill="var(--red)"/>
      <path d="M0 0 H393 V170 C330 240 230 250 160 232 C100 218 40 200 0 172 Z" fill="var(--blue)"/>
      <path d="M200 30 C260 20 330 70 393 60 V160 C350 120 280 110 230 90 Z" fill="#2a5fb3" opacity=".5"/>
    </svg>

    <div class="abs act-head">SOME OF THESE FUN ACTIVITIES INCLUDE:</div>
    <ul class="abs act-grid">
      <li class="tick">SNORKELING</li>
      <li class="tick">PADDLEBOARD</li>
      <li class="tick">UNDERWATER SCOOTER</li>
      <li class="tick">CLIFF DIVING</li>
      <li class="tick">SITE SEEING</li>
      <li class="tick">TUBING</li>
      <li class="tick">FLOATING</li>
      <li class="tick">SWIMMING</li>
    </ul>
    <p class="abs act-note">The Possibilities are endless on our charters. Just tell us what you want and we can make it happen!</p>

    <div class="abs photo photo-family" role="img" aria-label="Smiling family giving thumbs up aboard a sailboat"></div>
    <div class="abs photo photo-ray" role="img" aria-label="Swimmer with a stingray in clear shallow water"></div>

    <div class="abs types-bar">TYPES OF CHARTERS</div>
    <div class="abs timeline"></div>

    <article class="abs charter" style="top:354px">
      <span class="mark"></span>
      <h3>PRIVATE FULL DAY CHARTER- <span>8:30am-4:30pm</span></h3>
      <p>Embark on your full day charter with us at Tidewell! You will be greeted with "Champagne Mimosas" as we welcome you on the boat. You will then be given a brief introduction to our boat, safety rules and procedures, and stateroom assignments. Tidewell gives you the opportunity to customize your itinerary to snorkel, site see, or just relax. Some of the water sports that we offer are snorkeling, underwater scooter, cliff diving, swimming, floating, paddleboard, and tubing.</p>
    </article>

    <article class="abs charter" style="top:446px">
      <span class="mark"></span>
      <h3>PRIVATE HALF DAY CHARTER- <span>AM 8:30am-12:00 PM 1:00-4:30</span></h3>
      <p>Charter will start with "Welcome Mimosas" or "Champagne Cocktails" and a brief introduction to our boat, safety rules and procedures, and stateroom assignments for guests. Our fully customizable itinerary will allow your group to do things like snorkeling, site seeing, or just relaxing. Some watersports that we have available on board include snorkel, underwater scooter, cliff diving, swimming, floating, paddleboard, and tubing. We will sail to various destination spots surrounding St. Thomas and St. John. (not able to visit BVI)</p>
    </article>

    <article class="abs charter" style="top:558px">
      <span class="mark"></span>
      <h3>PRIVATE LUXURY FULL DAY "GLIMMER FEAST" CHARTER- <span>8:30am-4:30pm</span></h3>
      <p>Experience yacht charter service at its finest! Sail away with us on a Luxury Charter experience complete with a full brunch spread, specialty cocktails, and beautiful scenery and water activities. This experience includes it all. This full day experience will begin with "Welcome Mimosas" as you board our beautiful boat. You will then be given a brief introduction to our boat, safety rules and procedures, and stateroom assignments. Tidewell gives you the opportunity to customize your day to snorkel, site see, or just relax. As we sail to our first destination, you will enjoy a wide array of beverages including Mimosas, Bloody Mary Cocktails, and of course fresh brewed coffee and juice.</p>
    </article>

    <article class="abs charter" style="top:684px">
      <span class="mark"></span>
      <h3>PRIVATE SUNSET AND BUBBLES SAIL- <span>5:00-6:30pm</span></h3>
      <p>Set sail into the sunset, on our Sunset and Bubbles Sail. Enjoy appetizers such as seasonal fruits, veggies and cured meats, and appetizers. While relaxing as our exceptional crew sails you through the coveted scenic spots in the USVI. As the sun sets, the drinks will flow. Enjoy our "all you can drink" spectacular experience!</p>
    </article>

    <article class="abs charter" style="top:752px">
      <span class="mark"></span>
      <h3>PRIVATE LUXURY MINI OVERNIGHT WITH DINNER SAIL- <span>5:00pm-7:00am</span></h3>
      <p>Tidewell offers a USVI Mini Overnight getaway. We are extremely flexible and are able to offer a one night minimum. This charter can be booked solo, or combined with our above charter options to extend your time on the caribbean sea. Your luxury charter will start with a welcome "Champagne Cocktail," introduction to boat rules, safety and stateroom assignment. We will then set sail into the sunset while enjoying your open bar that includes beer, wine, champagne, soft drinks, and rum punch.</p>
    </article>
  </section>

</div>
</body>
</html>
```